Boutique town planning business needs a Business Card design

We need a business card design for a new company called The Zoning Bridgeway. We provide town planning and urban design services to government, business and community groups. We would like to see the designs use the colours in the logo (blue, deep red, green and amber), plenty of white and including black and grey in the writing. The final design should communicate collaboration, creativity and professionalism and that we are approachable.

```html
<!DOCTYPE html>
<html lang="en">
<head>
<meta charset="utf-8">
<title>The Zoning Bridgeway – Business Card</title>
<link rel="stylesheet" href="https://fonts.googleapis.com/css2?family=Exo+2:wght@400;600&display=swap">
<style>
  :root {
    --bg: #e6e6e4;
    --card: #ffffff;
    --black: #0d0d0d;
    --orange: #f07d12;
    --ink: #4a4a4a;
    --light: #f2f2f2;
    --mark: #3a9bc9;
  }
  * { box-sizing: border-box; margin: 0; padding: 0; }
  html, body { width: 1200px; height: 900px; overflow: hidden; }
  body {
    background: var(--bg);
    font-family: "Exo 2", sans-serif;
    position: relative;
  }
  .card {
    position: absolute;
    top: 225px;
    width: 500px;
    height: 450px;
    border-radius: 38px;
    background: var(--card);
    overflow: hidden;
    box-shadow: 0 6px 18px rgba(0,0,0,0.12);
  }
  .card--front { left: 60px; }
  .card--back { left: 640px; }
  .front-panel { position: absolute; inset: 0; }
  .contact {
    position: absolute;
    left: 34px;
    top: 44px;
    color: var(--light);
  }
  .contact__name {
    font-size: 18px;
    font-weight: 600;
    letter-spacing: 1.2px;
    text-transform: uppercase;
  }
  .contact__role {
    font-size: 13px;
    margin-top: 2px;
    letter-spacing: 0.4px;
  }
  .contact__address {
    font-size: 12px;
    line-height: 1.45;
    margin-top: 28px;
    letter-spacing: 0.3px;
  }
  .contact__list {
    list-style: none;
    margin-top: 28px;
    font-size: 12px;
    line-height: 1.75;
    letter-spacing: 0.3px;
  }
  .contact__list li { display: flex; align-items: center; gap: 8px; white-space: nowrap; }
  .contact__list svg { width: 11px; height: 11px; flex: none; }
  .brand {
    position: absolute;
    display: flex;
    align-items: center;
    gap: 12px;
    color: var(--ink);
    font-weight: 600;
    font-size: 21px;
    letter-spacing: 0.3px;
    white-space: nowrap;
  }
  .brand__dot {
    width: 46px;
    height: 46px;
    border-radius: 50%;
    background: var(--mark);
    flex: none;
  }
  .card--front .brand { left: 272px; top: 205px; font-size: 16px; gap: 10px; }
  .card--front .brand__dot { width: 34px; height: 34px; }
  .card--back .brand { left: 50%; top: 50%; transform: translate(-50%, -50%); }
</style>
</head>
<body>
  <section class="card card--front" aria-label="Business card front">
    <svg class="front-panel" viewBox="0 0 500 450" preserveAspectRatio="none" aria-hidden="true">
      <path d="M0 0 H280 C264 150 238 300 200 450 H0 Z" fill="var(--black)"/>
      <path d="M293 0 C277 150 251 300 213 450" fill="none" stroke="var(--orange)" stroke-width="7"/>
    </svg>
    <div class="contact">
      <p class="contact__name">Daniel Hartley</p>
      <p class="contact__role">Managing Director</p>
      <p class="contact__address">027 9th floor Plaza<br>Meridian Road KLT</p>
      <ul class="contact__list">
        <li>
          <svg viewBox="0 0 12 12" aria-hidden="true"><path d="M3 1 L5 3.5 L4 5 Q5 7 7 8 L8.5 7 L11 9 L9.5 11 Q5 11 1 5.5 Q1 2.5 3 1 Z" fill="currentColor"/></svg>
          012 555 0147
        </li>
        <li>
          <svg viewBox="0 0 12 12" aria-hidden="true"><rect x="3" y="0.5" width="6" height="11" rx="1.2" fill="none" stroke="currentColor" stroke-width="1.2"/><circle cx="6" cy="9.5" r="0.7" fill="currentColor"/></svg>
          012 555 0148
        </li>
        <li>
          <svg viewBox="0 0 12 12" aria-hidden="true"><rect x="3" y="1" width="6" height="3" fill="currentColor"/><rect x="1" y="4.5" width="10" height="4.5" rx="1" fill="currentColor"/><rect x="3" y="8" width="6" height="3" fill="none" stroke="currentColor"/></svg>
          012 555 0149
        </li>
        <li>
          <svg viewBox="0 0 12 12" aria-hidden="true"><rect x="0.7" y="2.2" width="10.6" height="7.6" rx="1" fill="none" stroke="currentColor" stroke-width="1.2"/><path d="M1 2.8 L6 6.8 L11 2.8" fill="none" stroke="currentColor" stroke-width="1.2"/></svg>
          hi@zoningbridge.com
        </li>
        <li>
          <svg viewBox="0 0 12 12" aria-hidden="true"><circle cx="6" cy="6" r="5" fill="none" stroke="currentColor" stroke-width="1.1"/><ellipse cx="6" cy="6" rx="2.2" ry="5" fill="none" stroke="currentColor" stroke-width="1"/><path d="M1 6 H11" stroke="currentColor" stroke-width="1"/></svg>
          www.zoningbridge.com
        </li>
      </ul>
    </div>
    <div class="brand">
      <span class="brand__dot"></span>
      <span class="brand__name">The Zoning Bridgeway</span>
    </div>
  </section>

  <section class="card card--back" aria-label="Business card back">
    <div class="brand">
      <span class="brand__dot"></span>
      <span class="brand__name">The Zoning Bridgeway</span>
    </div>
  </section>
</body>
</html>
```